Website Design for Australian Vocational Education organisation

A website for an Educational organisation. A responsive design that works well on a laptop desktop or a mobile phone. Is easy to navigate. Be able to start small and add new pages and features at a later stage.
Requires the logo, the name of company, home page with hero shots, enquiry form that forwards to a specified email address
links to social media, home page. We need a home page, and two more templates for sub pages.
Must not be a typical common design.

current website www.qvtl.edu.au
this needs to look different. logo should remain the same.

Target Market(s)

across age groups from 18-70. so must be inutitive. some will be tech savvy and others not.

Industry/Entity Type

Education

Coding

Coded - Design and coding required

Colors

Designer to choose colors to be used in the design.

Requirements
Must have
• responsive design, video, photo gallery, hero image, social media links, news feed, calendar, shopping cart, enquiry form
Nice to have
• Sample website
• www.bluegumlearning.com.au
• but should not be similar to this. it must look different. the sample is to give an idea on the various pages and links that will be required

```html
<!DOCTYPE html>
<html lang="en">
<head>
<meta charset="utf-8">
<title>Southern Institute of Applied Skills</title>
<link href="https://fonts.googleapis.com/css2?family=Roboto:wght@400;500;700&family=Montserrat:wght@600;700&display=swap" rel="stylesheet">
<style>
:root{
  --navy:#25256b;
  --navy-dark:#1f1f5c;
  --red:#d4102a;
  --ink:#333;
  --muted:#555;
  --grey:#efefef;
  --form-grey:#e6e6e6;
  --white:#fff;
}
*{box-sizing:border-box;margin:0;padding:0}
html,body{width:1200px;height:4196px;overflow:hidden}
body{font-family:"Roboto",Arial,sans-serif;color:var(--ink);background:var(--white);position:relative}
h1,h2,h3{font-family:"Montserrat",Arial,sans-serif;font-weight:700}

/* header */
.site-header{position:absolute;top:0;left:0;width:1200px;height:147px;background:var(--white)}
.brand{position:absolute;left:78px;top:22px;display:flex;align-items:center;gap:14px}
.brand-square{width:92px;height:92px;background:var(--navy)}
.brand-name{font-weight:700;font-size:19px;line-height:23px;color:var(--navy);text-transform:uppercase}
.main-nav{position:absolute;left:406px;top:0;height:147px;display:flex}
.main-nav a{display:block;height:147px;line-height:150px;padding:0 14px;font-size:15px;color:#444;text-decoration:none;text-transform:uppercase;position:relative}
.main-nav a.active{color:var(--red);font-weight:700}
.main-nav a.active::after{content:"";position:absolute;left:0;right:0;bottom:0;height:4px;background:var(--red)}

/* hero */
.hero{position:absolute;top:147px;left:0;width:1200px;height:548px;background:linear-gradient(90deg,#6b6f5c 0%,#8c8a7a 30%,#b9a893 55%,#a2584c 80%,#7d2a2a 100%)}
.hero-title{position:absolute;left:190px;top:215px;font-size:33px;color:var(--white);letter-spacing:.5px}
.search{position:absolute;left:112px;top:288px;width:567px;height:50px;background:var(--white);border-radius:25px;display:flex;align-items:center;padding-left:40px;font-size:18px;color:#333}
.search-btn{position:absolute;right:5px;top:5px;width:40px;height:40px;border-radius:50%;background:var(--navy)}
.hero-arrow{position:absolute;top:472px;width:36px;height:33px;background:var(--red)}

/* courses */
.courses{position:absolute;top:695px;left:0;width:1200px;height:415px;background:var(--navy)}
.section-title-light{position:absolute;top:40px;left:0;width:100%;text-align:center;color:var(--white);font-size:42px}
.course{position:absolute;top:160px;width:240px;margin-left:-120px;text-align:center;color:var(--white)}
.course svg{display:block;margin:0 auto 22px}
.course span{font-weight:700;font-size:22px}

/* about */
.about{position:absolute;top:1110px;left:0;width:1200px;height:511px;background:var(--white)}
.two-tone{font-size:40px;color:var(--navy)}
.two-tone em{font-style:normal;color:var(--red)}
.about h2{position:absolute;left:81px;top:70px}
.about h3{position:absolute;left:81px;top:140px;font-family:"Roboto",Arial,sans-serif;font-weight:700;font-size:22px;color:#555}
.about p{position:absolute;left:83px;top:192px;width:590px;font-size:14px;line-height:27.5px;color:#555}
.btn{display:inline-block;background:var(--red);color:var(--white);font-weight:700;font-size:15px;text-transform:uppercase;border-radius:25px;text-align:center;text-decoration:none}
.about .btn{position:absolute;left:75px;top:384px;width:150px;height:49px;line-height:49px}
.about-brand{position:absolute;left:768px;top:100px;width:277px;text-align:center}
.about-brand .mark{width:110px;height:110px;background:var(--navy);margin:0 auto 16px}
.about-brand .rule{height:4px;background:var(--navy);margin-bottom:10px}
.about-brand .name{font-weight:700;font-size:16px;line-height:18px;color:var(--navy);text-transform:uppercase}
.badge{position:absolute;top:331px;height:73px;background:#dcdcdc}

/* gallery */
.gallery{position:absolute;top:1621px;left:0;width:1200px;height:451px;background:var(--grey)}
.gallery h2{position:absolute;top:50px;width:100%;text-align:center}
.gallery-photo{position:absolute;top:137px;width:252px;height:223px}
.gallery-arrow{position:absolute;top:207px;width:39px;height:52px;background:var(--red)}

/* news */
.news{position:absolute;top:2072px;left:0;width:1200px;height:684px;background:var(--white)}
.news h2{position:absolute;top:50px;width:100%;text-align:center}
.news-card{position:absolute;top:139px;width:316px;text-align:center}
.news-photo{position:relative;width:316px;height:270px}
.news-date{position:absolute;left:110px;top:96px;width:96px;height:96px;border:4px solid rgba(255,255,255,.9);color:var(--white);text-align:center}
.news-date b{display:block;font-weight:400;font-size:44px;line-height:50px;margin-top:6px}
.news-date small{font-size:18px}
.news-card h4{margin-top:26px;font-weight:700;font-size:22px;line-height:28px;color:#222}
.news-card p{margin-top:8px;font-size:12px;line-height:22.5px;color:#444;padding:0 16px}
.news .btn{position:absolute;left:506px;top:598px;width:188px;height:47px;line-height:47px}

/* video */
.video{position:absolute;top:2756px;left:0;width:1200px;height:554px;background:linear-gradient(90deg,#3d4135 0%,#4c5343 35%,#5a5a52 60%,#6a625a 80%,#3c3d40 100%)}
.video-shade{position:absolute;inset:0;background:rgba(0,0,0,.3)}
.play{position:absolute;left:525px;top:192px}

/* contact */
.contact-info{position:absolute;top:3310px;left:0;width:531px;height:724px;background:var(--navy)}
.contact-info h2{position:absolute;left:73px;top:98px;font-size:38px;color:var(--white)}
.info-row{position:absolute;left:80px;display:flex;gap:16px;color:var(--white);font-size:15px;line-height:27px}
.info-row svg{flex:none;margin-top:6px}
.map{position:absolute;left:75px;top:410px;width:420px;height:239px;background:linear-gradient(135deg,#eeeae3,#e2e6ea)}
.enquiry{position:absolute;top:3310px;left:531px;width:669px;height:724px;background:var(--form-grey)}
.enquiry h2{position:absolute;left:34px;top:98px;font-size:38px;color:#111}
.enquiry p{position:absolute;left:37px;top:160px;font-size:15px;line-height:28px;color:#333}
.field{position:absolute;background:var(--white);font-size:14px;font-weight:700;color:#333;padding:14px 28px;text-transform:uppercase}
.robot{position:absolute;left:40px;top:433px;width:295px;height:76px;background:#f9f9f9;border:1px solid #d3d3d3;display:flex;align-items:center;padding-left:16px;font-size:15px;color:#222}
.robot i{width:26px;height:26px;border:2px solid #c1c1c1;background:var(--white);margin-right:14px}
.robot b{position:absolute;right:18px;top:18px;width:34px;height:34px;background:#c9d3e6}
.enquiry .submit{position:absolute;left:47px;top:542px;width:120px;height:39px;line-height:39px;background:var(--red);color:var(--white);font-weight:700;font-size:14px;text-align:center}

/* footer */
.site-footer{position:absolute;top:4034px;left:0;width:1200px;height:162px;background:var(--white)}
.footer-nav{position:absolute;top:32px;width:100%;display:flex;justify-content:center;gap:32px}
.footer-nav a{font-size:15px;color:#444;text-decoration:none;text-transform:uppercase}
.footer-nav a.active{color:var(--red);font-weight:700}
.social{position:absolute;top:76px;width:100%;display:flex;justify-content:center;gap:24px}
.social span{width:20px;height:20px;border-radius:50%;background:#222}
.copyright{position:absolute;top:114px;width:100%;text-align:center;font-size:12px;color:#222}
</style>
</head>
<body>

<header class="site-header">
  <div class="brand">
    <div class="brand-square"></div>
    <div class="brand-name">Southern<br>Institute of<br>Applied<br>Skills</div>
  </div>
  <nav class="main-nav">
    <a class="active" href="#">Home</a>
    <a href="#">About Us</a>
    <a href="#">Video</a>
    <a href="#">Photo Gallery</a>
    <a href="#">Courses</a>
    <a href="#">Students</a>
    <a href="#">Contact Us</a>
  </nav>
</header>

<section class="hero" role="img" aria-label="Smiling student holding an open book with classmates blurred behind">
  <h1 class="hero-title">HOW CAN WE HELP YOU?</h1>
  <div class="search">Search
    <span class="search-btn"><svg width="40" height="40" viewBox="0 0 40 40"><circle cx="19" cy="19" r="6" fill="none" stroke="#fff" stroke-width="2.5"/><line x1="23.5" y1="23.5" x2="28" y2="28" stroke="#fff" stroke-width="2.5"/></svg></span>
  </div>
  <span class="hero-arrow" style="left:560px"><svg width="36" height="33"><polyline points="20,11 14,16.5 20,22" fill="none" stroke="#fff" stroke-width="2.5"/></svg></span>
  <span class="hero-arrow" style="left:605px"><svg width="36" height="33"><polyline points="16,11 22,16.5 16,22" fill="none" stroke="#fff" stroke-width="2.5"/></svg></span>
</section>

<section class="courses">
  <h2 class="section-title-light">COURSES</h2>
  <div class="course" style="left:243px">
    <svg width="60" height="60" viewBox="0 0 60 60" fill="none" stroke="#fff" stroke-width="2.2"><ellipse cx="18" cy="16" rx="5" ry="7"/><ellipse cx="42" cy="16" rx="5" ry="7"/><ellipse cx="8" cy="31" rx="5" ry="6"/><ellipse cx="52" cy="31" rx="5" ry="6"/><path d="M30 30c-9 0-16 12-16 18 0 6 8 5 16 3 8 2 16 3 16-3 0-6-7-18-16-18z"/></svg>
    <span>ANIMAL CARE</span>
  </div>
  <div class="course" style="left:482px">
    <svg width="60" height="60" viewBox="0 0 60 60" fill="none" stroke="#fff" stroke-width="2.2"><rect x="3" y="14" width="54" height="40"/><path d="M22 14V6h16v8"/><line x1="3" y1="24" x2="57" y2="24"/><line x1="14" y1="10" x2="14" y2="18"/><line x1="46" y1="10" x2="46" y2="18"/></svg>
    <span>BUSINESS</span>
  </div>
  <div class="course" style="left:723px">
    <svg width="60" height="60" viewBox="0 0 60 60" fill="none" stroke="#fff" stroke-width="2.2"><path d="M30 12c-8-5-18-5-26-3v42c8-2 18-2 26 3 8-5 18-5 26-3V9c-8-2-18-2-26 3z"/><line x1="30" y1="12" x2="30" y2="54"/></svg>
    <span>EDUCATION</span>
  </div>
  <div class="course" style="left:962px">
    <svg width="60" height="60" viewBox="0 0 60 60" fill="none" stroke="#fff" stroke-width="2.2"><path d="M20 3h20v16a10 10 0 0 1-20 0z"/><line x1="20" y1="13" x2="40" y2="13"/><line x1="30" y1="29" x2="30" y2="52"/><line x1="22" y1="55" x2="38" y2="55"/></svg>
    <span>HOSPITALITY</span>
  </div>
</section>

<section class="about">
  <h2 class="two-tone">ABOUT <em>US</em></h2>
  <h3>Welcome to Southern Institute of Applied Skills</h3>
  <p>Southern Institute of Applied Skills (SIAS) is a Registered Training Organisation (RTO), is one of Australia's leading private training providers for individuals, businesses, community groups and Government, offering apprenticeships and certificate level training through to diplomas, SIAS offers the full extent of the tertiary experience and can help you identify a training pathway to help you reach your goals, whether you are new to study or already hold qualifications.</p>
  <a class="btn" href="#">Read More</a>
  <div class="about-brand">
    <div class="mark"></div>
    <div class="rule"></div>
    <div class="name">Southern Institute of<br>Applied Skills</div>
  </div>
  <div class="badge" style="left:770px;width:135px"></div>
  <div class="badge" style="left:928px;width:100px"></div>
</section>

<section class="gallery">
  <h2 class="two-tone">PHOTO <em>GALLERY</em></h2>
  <span class="gallery-arrow" style="left:34px"><svg width="39" height="52"><polyline points="23,19 16,26 23,33" fill="none" stroke="#fff" stroke-width="3"/></svg></span>
  <div class="gallery-photo" role="img" aria-label="Students studying together in a sunlit campus walkway" style="left:75px;background:linear-gradient(135deg,#a0583d,#d8cfc2)"></div>
  <div class="gallery-photo" role="img" aria-label="Group of students working around a table with plans" style="left:340px;background:linear-gradient(135deg,#5c5a55,#c9c2b6)"></div>
  <div class="gallery-photo" role="img" aria-label="Student with headphones reading in a library" style="left:606px;background:linear-gradient(135deg,#4c3326,#a57e5b)"></div>
  <div class="gallery-photo" role="img" aria-label="Students meeting in a bright seminar room" style="left:871px;background:linear-gradient(135deg,#3d3d3b,#d2c8b6)"></div>
  <span class="gallery-arrow" style="left:1124px"><svg width="39" height="52"><polyline points="16,19 23,26 16,33" fill="none" stroke="#fff" stroke-width="3"/></svg></span>
</section>

<section class="news">
  <h2 class="two-tone">LATEST <em>NEWS</em></h2>
  <article class="news-card" style="left:73px">
    <div class="news-photo" role="img" aria-label="Students working at laptops in class" style="background:linear-gradient(135deg,#4e5560,#b6b1aa)"><div class="news-date"><b>27</b><small>Apr</small></div></div>
    <h4>Lorem ipsum dolor sit<br>amet, consectetur</h4>
    <p>Sed ut perspiciatis unde omnis iste natus error sit voluptatem accusantium doloremque laudantium, totam rem aperiam, eaque ipsa quae</p>
  </article>
  <article class="news-card" style="left:441px">
    <div class="news-photo" role="img" aria-label="Colleagues giving a high five in an office" style="background:linear-gradient(135deg,#8a8a86,#e1dcd4)"><div class="news-date"><b>27</b><small>Apr</small></div></div>
    <h4>Lorem ipsum dolor sit<br>amet, consectetur</h4>
    <p>Sed ut perspiciatis unde omnis iste natus error sit voluptatem accusantium doloremque laudantium, totam rem aperiam, eaque ipsa quae</p>
  </article>
  <article class="news-card" style="left:809px">
    <div class="news-photo" role="img" aria-label="Students in blue shirts studying at a desk" style="background:linear-gradient(135deg,#3b4f72,#9aa7b4)"><div class="news-date"><b>27</b><small>Apr</small></div></div>
    <h4>Lorem ipsum dolor sit<br>amet, consectetur</h4>
    <p>Sed ut perspiciatis unde omnis iste natus error sit voluptatem accusantium doloremque laudantium, totam rem aperiam, eaque ipsa quae</p>
  </article>
  <a class="btn" href="#">View Calendar</a>
</section>

<section class="video" role="img" aria-label="Video still of a student working on a laptop outdoors">
  <div class="video-shade"></div>
  <svg class="play" width="150" height="150" viewBox="0 0 150 150"><circle cx="75" cy="75" r="70" fill="none" stroke="rgba(255,255,255,.75)" stroke-width="8"/><polygon points="58,45 58,105 108,75" fill="#fff"/></svg>
</section>

<section class="contact-info">
  <h2>CONTACT US</h2>
  <div class="info-row" style="top:200px"><svg width="14" height="16" viewBox="0 0 14 16"><path d="M7 0a6 6 0 0 0-6 6c0 4 6 10 6 10s6-6 6-10a6 6 0 0 0-6-6z" fill="#fff"/><circle cx="7" cy="6" r="2.2" fill="#25256b"/></svg><span>18 Harbour Lane, Eastfield<br>ACT 2690</span></div>
  <div class="info-row" style="top:283px"><svg width="14" height="14" viewBox="0 0 14 14"><path d="M3 0l3 3-2 2c1 2 3 4 5 5l2-2 3 3-2 3C6 14 0 8 0 3z" fill="#fff"/></svg><span>+61 400 123 456</span></div>
  <div class="info-row" style="top:310px"><svg width="14" height="12" viewBox="0 0 14 12"><rect y="1" width="14" height="10" fill="#fff"/><polyline points="0,1 7,7 14,1" fill="none" stroke="#25256b" stroke-width="1.4"/></svg><span>hello@southernapplied.example</span></div>
  <div class="map" role="img" aria-label="Street map showing the campus location"></div>
</section>

<section class="enquiry">
  <h2>GET IN TOUCH</h2>
  <p>Let us paddle the canoe in unison, lest we are swamped by the waves.<br>Rangi, Te Awa</p>
  <div class="field" style="left:37px;top:255px;width:270px;height:46px">Name</div>
  <div class="field" style="left:322px;top:255px;width:270px;height:46px">Email</div>
  <div class="field" style="left:37px;top:314px;width:555px;height:99px">Message</div>
  <div class="robot"><i></i>I'm not a robot<b></b></div>
  <div class="submit">SUBMIT</div>
</section>

<footer class="site-footer">
  <nav class="footer-nav">
    <a class="active" href="#">Home</a>
    <a href="#">About Us</a>
    <a href="#">Video</a>
    <a href="#">Photo Gallery</a>
    <a href="#">Courses</a>
    <a href="#">Students</a>
    <a href="#">Contact Us</a>
  </nav>
  <div class="social"><span></span><span></span><span></span></div>
  <div class="copyright">© 2019 SIAS. Southern Institute of Applied Skills Pty Ltd | ACN: 600000001 | RTO: 10001.</div>
</footer>

</body>
</html>
```